Flyer Kora 7
Zielgruppe
Einkaufsgemeinschaft
Aufgabenstellung
Anmerkungen:
"Unser Kora 7 Logo bitte als eine Art Wasserzeichen einfügen: (evtl. schräg längs)
Firmenfarben sind: Blau, Schwarz und Weiß"
Größe: DinA4"
Unsere Unternehmen hat es sich zur Aufgabe gemacht, durch den gemeinsamen Einkauf eine "Win-Win- Situation" zu schaffen.
Keine Aufnahmegebühr und keine monatlichen Kosten – Mitgliedschaft ist kostenfrei
Unkomplizierte Abwicklung – Sie kaufen weiterhin beim Großhändler Ihres Vertrauens
Preisvorteile für Sie, durch gemeinsame Bündelung des Einkaufsvolumens
Für jede Betriebsgröße geeignet
Kompetente Betreuung
Vergütungsbeispiele in Höhe von z.B. 3-5 % Ersparnis vom Wareneinkauf
3.000 € WE, Ihre Ersparnis 90 € x 12 Monate = 1.080 € - 360 € = 720 € (Endbetrag jeweils Hervorheben Bsp. 720 €)
4.000 € WE, Ihre Ersparnis 120 € x 12 Monate = 1.440 € - 480 € = 960 €
5.000 € WE, Ihre Ersparnis 150 € x 12 Monate = 1.800 € - 600 € = 1.200 €
7.500 € WE, Ihre Ersparnis 225 € x 12 Monate = 2.700 € - 900 € = 1.800 €
10.000 € WE, Ihre Ersparnis 300 x 12 Monate = 3.600 € - 1.200 € = 2.400 €
15.000 € WE, Ihre Ersparnis 450 € x 12 Monate = 5.400 € - 1.800 € = 3.600 €
20.000 € WE, Ihre Ersparnis 600 € x 12 Monate = 7.200 € - 2.400 € = 4.800 €
Ausschüttung erfolgt transparent
Geschäftsführung:
Fachmann für Steuerrecht, langjährige Erfahrung in der Betreuung von Gastronomen
Betriebswirt (VWA), langjährige Erfahrung im operativen und strategischen Einkauf

```html
<!DOCTYPE html>
<html lang="de">
<head>
<meta charset="utf-8">
<title>Flyer Kora 7</title>
<link href="https://fonts.googleapis.com/css2?family=Oswald:wght@400;500&family=Pathway+Gothic+One&display=swap" rel="stylesheet">
<style>
  :root{
    --sky:#00b8e6;
    --sky-light:#7fcbe8;
    --blue:#0a86c8;
    --blue-deep:#0670b0;
    --ink:#333539;
    --ink-dark:#2e2f33;
    --accent-text:#2f4756;
    --grey:#9a9a9a;
    --paper:#ededed;
    --stage:#d4dbe3;
    --white:#ffffff;
  }
  *{margin:0;padding:0;box-sizing:border-box}
  html,body{width:1200px;height:797px;overflow:hidden}
  body{background:var(--stage);font-family:"Pathway Gothic One",sans-serif;position:relative}
  .flyer{position:absolute;left:325px;top:10px;width:550px;height:777px;
    background:linear-gradient(180deg,#f3f3f3 0%,#e6e6e6 60%,#d4d4d4 100%);overflow:hidden;
    box-shadow:0 6px 18px rgba(0,0,0,.18)}
  .hero-visual{position:absolute;left:0;top:0;width:373px;height:186px;
    background:radial-gradient(ellipse at 55% 55%,#ffffff 0%,#e4e6e8 70%,#cfd3d6 100%)}
  .benefits{position:absolute;left:388px;top:0;width:162px;height:186px;background:var(--sky);
    list-style:none;padding:28px 0 0 22px}
  .benefits li{display:flex;gap:7px;color:var(--ink);font-size:18px;line-height:18px;margin-bottom:12px}
  .benefits svg{flex:none;width:18px;height:14px;margin-top:2px}
  .intro{position:absolute;left:0;top:201px;width:373px;height:68px;background:var(--sky);
    color:var(--white);padding:12px 0 0 19px;overflow:hidden}
  .intro-line{display:block;white-space:nowrap;font-size:16px;line-height:22px;
    transform:scaleX(.84);transform-origin:left center}
  .intro em{font-style:normal;color:var(--accent-text)}
  .team-photo{position:absolute;left:388px;top:201px;width:162px;height:68px;
    background:linear-gradient(135deg,#e9eef2 0%,#b9aaa0 45%,#6f7880 100%)}
  .section-title{position:absolute;left:0;width:100%;top:290px;text-align:center;
    font-family:"Oswald",sans-serif;font-weight:400;font-size:29px;color:var(--ink);letter-spacing:-.5px;transform:scaleX(.78)}
  .section-sub{position:absolute;left:0;width:100%;top:321px;text-align:center;color:var(--blue);
    font-size:19px;font-style:italic}
  .col{position:absolute;top:358px;height:299px}
  .col-head{height:28px;display:flex;align-items:center;justify-content:center;
    font-family:"Oswald",sans-serif;font-weight:400;font-size:14px;color:var(--white)}
  .col-body{position:absolute;top:33px;bottom:0;left:0;right:0;display:flex;flex-direction:column;
    justify-content:space-around;align-items:center;padding:4px 0}
  .side-left{left:0;width:68px}
  .side-left .col-head{background:var(--sky-light)}
  .side-left .col-body{background:linear-gradient(180deg,#8fd0ee,#5bb3e0)}
  .purchase{left:74px;width:108px}
  .purchase .col-head{background:var(--blue)}
  .purchase .col-body{background:linear-gradient(180deg,#0a8ccd,#0670b0);color:var(--white);font-size:24px}
  .savings{left:187px;width:177px;border:4px solid var(--blue);background:linear-gradient(180deg,#ededed,#dcdcdc)}
  .savings .col-head{color:var(--blue);height:26px;border-bottom:3px solid var(--blue);margin:0 -1px}
  .savings .col-body{top:29px;color:var(--blue);font-size:13.5px;font-style:italic}
  .yearly{left:369px;width:108px}
  .yearly .col-head{background:var(--ink-dark)}
  .yearly .col-body{background:var(--ink-dark);color:var(--white);font-family:"Oswald",sans-serif;font-weight:500;font-size:21px}
  .yearly .col-body span{text-decoration:underline;text-underline-offset:3px;text-decoration-thickness:1px}
  .side-right{left:482px;width:68px}
  .side-right .col-head{background:var(--grey)}
  .side-right .col-body{background:linear-gradient(180deg,#a8a8a8,#8a8a8a)}
  .footer{position:absolute;left:0;top:657px;width:550px;height:120px;
    background:linear-gradient(180deg,#eaeaea,#d8d8d8)}
  .contact{position:absolute;top:18px;color:var(--ink);font-size:11px;line-height:12px}
  .contact-left{left:19px}
  .contact-right{right:27px;text-align:right}
  .contact h3{font-family:"Oswald",sans-serif;font-weight:500;font-size:14px;color:var(--blue);margin-bottom:3px;line-height:18px}
  .contact .reach{color:var(--blue);font-size:12.5px;line-height:14px;margin-top:6px}
  .brand{position:absolute;left:170px;top:22px;width:210px;text-align:center}
  .brand-name{display:flex;align-items:center;justify-content:center;gap:8px;
    font-family:"Oswald",sans-serif;font-weight:500;font-size:42px;line-height:48px;color:var(--blue)}
  .brand-name i{display:block;width:26px;height:26px;background:var(--blue)}
  .brand-tag{font-size:10px;letter-spacing:4px;color:var(--ink);margin-top:4px}
</style>
</head>
<body>
<main class="flyer">
  <div class="hero-visual" role="img" aria-label="Skizzen mit Diagrammen, Pfeilen und Schriftzug 100% Kompetenz"></div>

  <ul class="benefits">
    <li><svg viewBox="0 0 18 14"><path d="M1 7l5 5L17 1" fill="none" stroke="#333539" stroke-width="3"/></svg>Unkomplizierte<br>Abwicklung</li>
    <li><svg viewBox="0 0 18 14"><path d="M1 7l5 5L17 1" fill="none" stroke="#333539" stroke-width="3"/></svg>Für alle Betriebs-<br>größen geeignet</li>
    <li><svg viewBox="0 0 18 14"><path d="M1 7l5 5L17 1" fill="none" stroke="#333539" stroke-width="3"/></svg>Kompetente<br>Betreuung</li>
  </ul>

  <p class="intro">
    <span class="intro-line">Sie kaufen weiterhin beim <em>Großhändler Ihres Vertrauens</em> Preisvorteile für</span>
    <span class="intro-line">Sie, durch <em>gemeinsame Bündelung</em> des Einkaufsvolumens.</span>
  </p>

  <div class="team-photo" role="img" aria-label="Foto eines Teams im Besprechungsraum"></div>

  <h2 class="section-title">VERGÜTUNGSBEISPIELE</h2>
  <p class="section-sub">in Höhe von z.B. 3-5 % Ersparnis vom Wareneinkauf</p>

  <section class="col side-left"><div class="col-head"></div><div class="col-body"></div></section>

  <section class="col purchase">
    <div class="col-head">WARENEINKAUF</div>
    <div class="col-body">
      <span>3.000 €</span><span>4.000 €</span><span>5.000 €</span><span>7.500 €</span>
      <span>10.000 €</span><span>15.000 €</span><span>20.000 €</span>
    </div>
  </section>

  <section class="col savings">
    <div class="col-head">IHRE ERSPARNIS</div>
    <div class="col-body">
      <span>90 € x 12 Monate = 1.080 € - 360 €</span>
      <span>120 € x 12 Monate = 1.440 € - 480 €</span>
      <span>150 € x 12 Monate = 1.800 € - 600 €</span>
      <span>225 € x 12 Monate = 2.700 € - 900 €</span>
      <span>300 € x 12 Monate = 3.600 € - 1.200 €</span>
      <span>450 € x 12 Monate = 5.400 € - 1.800 €</span>
      <span>600 € x 12 Monate = 7.200 € - 2.400 €</span>
    </div>
  </section>

  <section class="col yearly">
    <div class="col-head">JAHRESERSPARNIS</div>
    <div class="col-body">
      <span>720 €</span><span>960 €</span><span>1.200 €</span><span>1.800 €</span>
      <span>2.400 €</span><span>3.600 €</span><span>4.800 €</span>
    </div>
  </section>

  <section class="col side-right"><div class="col-head"></div><div class="col-body"></div></section>

  <footer class="footer">
    <div class="contact contact-left">
      <h3>Martin Oberhaus</h3>
      <p>Fachmann für Steuerrecht, langjährige<br>Erfahrung in der Betreuung von Gastronomen</p>
      <p class="reach">Mobil: 0152 / 0000 4821<br>E-Mail: info@kora7-einkauf.de</p>
    </div>
    <div class="brand">
      <div class="brand-name">Kora 7<i></i></div>
      <div class="brand-tag">BESCHAFFUNGSMANAGEMENT</div>
    </div>
    <div class="contact contact-right">
      <h3>Stefan Kellner</h3>
      <p>Betriebswirt (VWA), langjährige Erfahrung im<br>operativen und strategischen Einkauf</p>
      <p class="reach">Mobil: 0170 / 000 7364<br>E-Mail: info@kora7-einkauf.de</p>
    </div>
  </footer>
</main>
</body>
</html>
```